FOLI PACK FOR STICKS

Design the packaging for salted sticks (weight 400g) reference to the logo VOLK (in attached).
Color packaging- look forward to suggestions.
Package with window.
Hi, we need only graphic conception without texts on back side.

Please find Logo VOLK and the grid of packaging - attached
Updates

Target Market(s)

typical salted snack for everyone (adults and children included)

Font styles to use
Sans Serif

Requirements
Should not have
• - religion and politic signs…
• - toys and childdraws
• - monsters, devils and demons etc.

```html
<!DOCTYPE html>
<html lang="en">
<head>
<meta charset="utf-8">
<title>VOLK Salted Sticks – Pack Front</title>
<link href="https://fonts.googleapis.com/css2?family=Nunito:wght@800&family=Courgette&display=swap" rel="stylesheet">
<style>
  :root {
    --backdrop: #eee5d8;
    --gold: #e9b73c;
    --gold-light: #f3cd5e;
    --cream: #fbefd2;
    --brown: #6b4524;
    --brown-dark: #553418;
    --dot: #7a5230;
    --window-light: #e7b27a;
    --window-dark: #b97838;
  }
  * { box-sizing: border-box; margin: 0; padding: 0; }
  html, body {
    width: 1200px;
    height: 1000px;
    overflow: hidden;
    background: var(--backdrop);
  }
  .canvas {
    position: relative;
    width: 1200px;
    height: 1000px;
  }
  .pack {
    position: absolute;
    left: 415px;
    top: 150px;
    width: 370px;
    height: 700px;
    background: var(--cream);
    box-shadow: 0 6px 18px rgba(60, 35, 10, 0.25);
    overflow: hidden;
  }
  .pack > * { position: absolute; left: 0; width: 100%; }

  .gold-cap { background: var(--gold); height: 36px; }
  .gold-cap--top { top: 0; }
  .gold-cap--bottom { bottom: 0; height: 22px; }

  .stripe-field {
    background: linear-gradient(90deg, var(--cream), #e2c58e 30%, #c9a06a 50%, #e2c58e 70%, var(--cream));
  }
  .stripe-field--top { top: 36px; height: 80px; }
  .stripe-field--bottom { top: 590px; height: 88px; }

  .brand-band {
    top: 116px;
    height: 112px;
    background: linear-gradient(180deg, var(--gold-light), var(--gold));
    border-top: 4px dotted var(--dot);
    border-bottom: 4px dotted var(--dot);
    display: flex;
    align-items: center;
    justify-content: center;
  }
  .brand-name {
    font-family: "Nunito", sans-serif;
    font-weight: 800;
    font-size: 64px;
    letter-spacing: 1px;
    color: var(--brown-dark);
    line-height: 1;
  }

  .product-window {
    top: 233px;
    height: 245px;
    background: linear-gradient(90deg, var(--window-light), var(--window-dark) 18%, var(--window-light) 32%, var(--window-dark) 48%, var(--window-light) 62%, var(--window-dark) 78%, var(--window-light));
  }

  .name-band {
    top: 480px;
    height: 108px;
    background: var(--cream);
    border-top: 4px dotted var(--dot);
    border-bottom: 4px dotted var(--dot);
    display: flex;
    align-items: center;
    justify-content: center;
  }
  .product-name {
    font-family: "Courgette", cursive;
    font-size: 42px;
    color: var(--brown);
    text-shadow: 0 0 3px #fff, 0 0 3px #fff, 0 0 3px #fff;
    line-height: 1;
  }
</style>
</head>
<body>
  <main class="canvas">
    <section class="pack">
      <div class="gold-cap gold-cap--top"></div>
      <div class="stripe-field stripe-field--top" role="img" aria-label="Vertical stripes in brown, cream and gold"></div>
      <div class="brand-band">
        <span class="brand-name">VOLK</span>
      </div>
      <div class="product-window" role="img" aria-label="Window showing golden baked sesame salted sticks"></div>
      <div class="name-band">
        <h1 class="product-name">Salted Sticks</h1>
      </div>
      <div class="stripe-field stripe-field--bottom" role="img" aria-label="Vertical stripes in brown, cream and gold"></div>
      <div class="gold-cap gold-cap--bottom"></div>
    </section>
  </main>
</body>
</html>
```